Brit Rock covers band "The Tin Kettles" requires poster for Fernhollow Club Friday March 31st

I want a design for a poster (A3 and A4) and Facebook/Instagram ads.
Primary focus is the band name logo "The Tin Kettles", style as in attached file, followed by tag "Old Skool Brit Rock".
Backdrop to be 60's psychedelic art.
Secondary focus is the venue "The Fernhollow Club"
Supporting text to include:
- 27 Quill Street, Chatswood SYDNEY
- Friday 31st March 2023
- 7:00 pm until late
- Bar sales refreshments
- NO admission fee

```html
<!DOCTYPE html>
<html lang="en">
<head>
<meta charset="utf-8">
<title>The Tin Kettles – The Fernhollow Club</title>
<link rel="stylesheet" href="https://fonts.googleapis.com/css2?family=Oswald:wght@500;700&family=Open+Sans:wght@700;800&display=swap">
<style>
  :root {
    --stage: #2a2a2d;
    --sky: #1fa0d0;
    --magenta: #d93a8c;
    --sun: #f3d33a;
    --violet: #4a3a8f;
    --navy: #231d64;
    --apricot: #f0ad55;
    --white: #ffffff;
  }
  * { box-sizing: border-box; margin: 0; padding: 0; }
  html, body {
    width: 1200px;
    height: 675px;
    overflow: hidden;
    background: var(--stage);
  }
  .poster {
    position: absolute;
    left: 375px;
    top: 19px;
    width: 450px;
    height: 636px;
    overflow: hidden;
    background: var(--sky);
  }
  .psychedelic-backdrop {
    position: absolute;
    inset: 0;
    background:
      radial-gradient(circle at 60% 45%, rgba(243, 211, 58, 0.45) 0%, rgba(243, 211, 58, 0) 45%),
      linear-gradient(135deg, var(--sky) 0%, #3aa8d4 35%, rgba(217, 58, 140, 0.55) 70%, var(--violet) 100%);
  }
  .band-name {
    position: absolute;
    left: 18px;
    top: 40px;
    width: 420px;
    font-family: "Oswald", sans-serif;
    font-weight: 700;
    color: var(--navy);
    text-transform: uppercase;
    line-height: 1;
    letter-spacing: -1px;
  }
  .band-name__first { display: block; font-size: 122px; }
  .band-name__second { display: block; font-size: 118px; margin-top: 4px; padding-left: 14px; }
  .venue {
    position: absolute;
    left: 179px;
    top: 310px;
    width: 258px;
    height: 52px;
    background: var(--navy);
    color: var(--white);
    font-family: "Oswald", sans-serif;
    font-weight: 500;
    font-size: 28px;
    font-variant: small-caps;
    display: flex;
    align-items: center;
    justify-content: center;
    white-space: nowrap;
    letter-spacing: -0.5px;
  }
  .address {
    position: absolute;
    left: 115px;
    top: 389px;
    width: 335px;
    height: 43px;
    background: var(--magenta);
    color: var(--white);
    font-family: "Oswald", sans-serif;
    font-weight: 500;
    font-size: 21px;
    display: flex;
    align-items: center;
    justify-content: center;
    white-space: nowrap;
  }
  .when {
    position: absolute;
    left: 0;
    top: 442px;
    width: 450px;
    height: 75px;
    background: var(--apricot);
    color: var(--magenta);
    font-family: "Open Sans", sans-serif;
    font-weight: 800;
    font-size: 26px;
    line-height: 32px;
    text-align: center;
    display: flex;
    flex-direction: column;
    justify-content: center;
  }
  .refreshments {
    position: absolute;
    left: 14px;
    top: 538px;
    color: var(--violet);
    font-family: "Open Sans", sans-serif;
    font-weight: 800;
    font-size: 26px;
    white-space: nowrap;
  }
  .admission {
    position: absolute;
    left: 0;
    bottom: 0;
    width: 450px;
    height: 48px;
    background: var(--navy);
    color: var(--white);
    font-family: "Open Sans", sans-serif;
    font-weight: 800;
    font-size: 25px;
    display: flex;
    align-items: center;
    justify-content: center;
  }
</style>
</head>
<body>
  <main class="poster">
    <div class="psychedelic-backdrop" role="img" aria-label="1960s psychedelic backdrop of radiating zigzag lines in blue, magenta, yellow and violet"></div>

    <h1 class="band-name">
      <span class="band-name__first">The Tin</span>
      <span class="band-name__second">Kettles</span>
    </h1>

    <p class="venue">The Fernhollow Club</p>
    <p class="address">27 Quill Street, Chatswood SYDNEY</p>

    <p class="when">
      <span>Friday 31st March 2023</span>
      <span>7:00 pm until late</span>
    </p>

    <p class="refreshments">Bar sales refreshments</p>
    <p class="admission">NO admission fee</p>
  </main>
</body>
</html>
```